Pool Screen Enclosure Building a Career Boot Camp!

Looking to Host a Boot Camp for people looking for a career or looking to change careers. We Design, Manufacture and Install Custom Pool Screen Enclosures. We have a training program to allow Non Experienced motivated people the chance at a great career that will provide a great living for them and their family. This will be a paid boot camp, week long, we provide all the initial training for them to make a transition into our business. This will be 5 days of training with a guaranteed job to start the following Monday.... This is good for both someone with no construction experience or someone with construction experience that wants to upgrade their current job.
Paid Boot Camp
transition to a full time job with great pay
Benefits include Health Insurance, Dental and Vision, 401K, we provide the tools and training.

```html
<!DOCTYPE html>
<html lang="en">
<head>
<meta charset="utf-8">
<title>Paid Boot Camp Flyer</title>
<link href="https://fonts.googleapis.com/css2?family=Oswald:wght@500;600;700&family=Varela+Round&family=Cormorant+Garamond:ital,wght@1,600&display=swap" rel="stylesheet">
<style>
  :root {
    --green: #66cc33;
    --green-text: #6cc93b;
    --black: #000000;
    --white: #ffffff;
    --cream: #eadcb0;
    --page: #ffffff;
  }
  * { margin: 0; padding: 0; box-sizing: border-box; }
  html, body { width: 1200px; height: 675px; overflow: hidden; background: var(--page); }
  .canvas { position: relative; width: 1200px; height: 675px; }
  .flyer {
    position: absolute; left: 353px; top: 17px;
    width: 494px; height: 640px; background: var(--black); overflow: hidden;
    font-family: 'Varela Round', sans-serif;
  }
  .flyer-shapes { position: absolute; inset: 0; }
  .brand { position: absolute; left: 104px; top: 32px; display: flex; align-items: center; gap: 10px; }
  .brand-dot { width: 30px; height: 30px; border-radius: 50%; background: var(--green); }
  .brand-name { font-family: 'Varela Round', sans-serif; color: var(--green-text); font-size: 25px; line-height: 1; }
  .brand-tagline {
    position: absolute; left: 190px; top: 61px;
    font-family: 'Cormorant Garamond', serif; font-style: italic; font-weight: 600;
    font-size: 12.5px; color: var(--cream);
  }
  .hero-title {
    position: absolute; left: 15px; top: 240px; color: var(--white);
    font-family: 'Oswald', sans-serif; font-weight: 700; text-transform: uppercase; line-height: 1;
  }
  .hero-title .paid { display: block; font-size: 54px; font-style: italic; letter-spacing: -1px; }
  .hero-title .camp { display: block; font-size: 58px; letter-spacing: -1px; margin-top: -6px; }
  .hero-sub {
    position: absolute; left: 15px; top: 344px; color: var(--white);
    font-family: 'Oswald', sans-serif; font-weight: 500; font-size: 14.5px;
    text-transform: uppercase; letter-spacing: -0.3px; transform: scaleX(0.9); transform-origin: left;
  }
  .benefits { position: absolute; left: 19px; top: 390px; color: var(--white); }
  .benefits h2 { font-family: 'Varela Round', sans-serif; font-weight: 400; font-size: 15.5px; line-height: 1.1; }
  .benefits ul { list-style: none; }
  .benefits li { display: flex; align-items: center; gap: 6px; font-size: 13px; line-height: 14px; }
  .benefits svg { width: 14px; height: 12px; flex: none; }
  .headline {
    position: absolute; left: 0; right: 0; top: 492px; text-align: center; color: var(--white);
    font-family: 'Oswald', sans-serif; font-weight: 600; font-style: italic; font-size: 26px;
    line-height: 28px; text-transform: uppercase; letter-spacing: -0.5px;
  }
  .divider { position: absolute; left: 177px; top: 558px; width: 140px; height: 2px; background: var(--green); }
  .address {
    position: absolute; left: 0; right: 0; top: 566px; text-align: center;
    color: var(--green-text); font-size: 12.5px; line-height: 15.5px;
  }
  .contact-email { position: absolute; left: 13px; top: 608px; display: flex; align-items: center; gap: 6px; color: var(--green-text); font-size: 12px; }
  .contact-email svg { width: 21px; height: 15px; }
  .contact-phone { position: absolute; right: 9px; top: 601px; display: flex; align-items: center; gap: 8px; color: var(--green-text); font-size: 21px; }
  .contact-phone svg { width: 21px; height: 21px; }
</style>
</head>
<body>
<main class="canvas">
  <article class="flyer">
    <svg class="flyer-shapes" viewBox="0 0 494 640" width="494" height="640">
      <defs>
        <linearGradient id="sky" x1="0" y1="0" x2="0" y2="1">
          <stop offset="0" stop-color="#9a9ea6"/>
          <stop offset="0.55" stop-color="#7b8089"/>
          <stop offset="0.8" stop-color="#5f6b61"/>
          <stop offset="1" stop-color="#6b8a8e"/>
        </linearGradient>
      </defs>
      <polygon points="0,88 208,99 0,110" fill="var(--green)"/>
      <polygon class="hero-photo" role="img" aria-label="Photo of a screened pool enclosure overlooking a lake at dusk"
               points="0,108 208,99 494,112 494,359 267,359 250,376 0,376" fill="url(#sky)"/>
      <rect x="0" y="376" width="494" height="103" fill="var(--green)"/>
      <polygon points="267,359 494,359 494,372 274,372 258,386 244,386 250,376" fill="var(--white)"/>
      <rect x="272" y="372" width="222" height="100" fill="var(--white)"/>
      <rect role="img" aria-label="Photo of a crew reviewing plans on site" x="276" y="376" width="69" height="91" fill="#8b8378"/>
      <rect role="img" aria-label="Photo of installers on an enclosure roof" x="347" y="376" width="67" height="91" fill="#7d94a8"/>
      <rect role="img" aria-label="Photo of an enclosure frame under construction" x="417" y="376" width="68" height="91" fill="#6f7269"/>
      <rect x="0" y="633" width="494" height="7" fill="var(--green)"/>
    </svg>

    <div class="brand"><span class="brand-dot"></span><span class="brand-name">The Lanai Works</span></div>
    <p class="brand-tagline">“Screen it in, so you can live in it”</p>

    <h1 class="hero-title"><span class="paid">Paid</span><span class="camp">Boot Camp</span></h1>
    <p class="hero-sub">Transition to a full time job with great pay</p>

    <section class="benefits">
      <h2>Benefits :</h2>
      <ul>
        <li><svg viewBox="0 0 14 12"><path d="M1 6.5 5 10 13 1.5" fill="none" stroke="#fff" stroke-width="2.6"/></svg>Health Insurance</li>
        <li><svg viewBox="0 0 14 12"><path d="M1 6.5 5 10 13 1.5" fill="none" stroke="#fff" stroke-width="2.6"/></svg>Dental and Vision</li>
        <li><svg viewBox="0 0 14 12"><path d="M1 6.5 5 10 13 1.5" fill="none" stroke="#fff" stroke-width="2.6"/></svg>401K</li>
        <li><svg viewBox="0 0 14 12"><path d="M1 6.5 5 10 13 1.5" fill="none" stroke="#fff" stroke-width="2.6"/></svg>We provide the tools and training</li>
      </ul>
    </section>

    <p class="headline">5 days of training with a guaranteed job to<br>start the following Monday</p>
    <div class="divider"></div>
    <p class="address">The Lanai Works<br>418 W Coral Avenue, Palm Harbor FL 34000</p>

    <p class="contact-email">
      <svg viewBox="0 0 21 15"><rect x="1" y="1" width="19" height="13" fill="none" stroke="#fff" stroke-width="1.6"/><path d="M1 1 10.5 8.5 20 1M1 14 8 7.5M20 14 13 7.5" fill="none" stroke="#fff" stroke-width="1.4"/></svg>
      hello@thelanaiworks.com
    </p>
    <p class="contact-phone">
      <svg viewBox="0 0 21 21"><circle cx="10.5" cy="10.5" r="10.5" fill="#fff"/><path d="M7 5.2c.6-.4 1.2-.3 1.5.3l1 2c.2.5.1.9-.3 1.2l-.8.6c.6 1.4 1.6 2.5 3 3.2l.6-.8c.3-.4.8-.5 1.2-.3l2 1c.6.3.7.9.3 1.5-.8 1.1-2 1.5-3.2 1-2.9-1.2-5-3.3-6.2-6.2-.5-1.2-.1-2.5 1-3.3z" fill="#000"/></svg>
      555-014-2739
    </p>
  </article>
</main>
</body>
</html>
```